Kestrel Roofpower Company need Flier for Bureau of Fuel Planning

We need a 2 page flier for distributing to Military Contractors and Bureau of Fuel Planning. We install residential solar and this will be used for military base housing and other gov. projects on the residential home communities. We need to show how large of a company we are and how we are able to work with the military //gov. projects. Attached is our website and other marketing info for your use. Thanks and good luck!

Target Market(s)

Military and Government Contractors //Bureau of Fuel Planning

Industry/Entity Type

Solar Energy

Requirements
Must have
• Our Why - Statement included

```html
<!DOCTYPE html>
<html lang="en">
<head>
<meta charset="utf-8">
<title>Kestrel Roofpower – Solar Flier</title>
<link href="https://fonts.googleapis.com/css2?family=Hind:wght@400;500;600;700&family=Roboto+Condensed:wght@700&family=Exo+2:ital,wght@0,500;1,700&display=swap" rel="stylesheet">
<style>
:root{
  --stage:#3b3b3d;
  --paper:#e9f4fb;
  --blue:#1c95d4;
  --blue-deep:#1480c0;
  --green:#8cc63f;
  --green-deep:#6fae2a;
  --ink:#222;
  --muted:#444;
  --white:#fff;
  --grey:#6e6e6e;
}
*{box-sizing:border-box;margin:0;padding:0}
html,body{width:1200px;height:809px;overflow:hidden;background:var(--stage)}
body{position:relative;font-family:"Hind",sans-serif;color:var(--ink)}
.page{position:absolute;top:58px;width:546px;height:708px;background:var(--paper);overflow:hidden;box-shadow:4px 6px 14px rgba(0,0,0,.45)}
.page--process{left:37px}
.page--solar{left:610px}
.abs{position:absolute}
.shapes{position:absolute;inset:0}
.photo{position:absolute}

/* process page */
.easy-title{left:0;width:546px;top:26px;text-align:center;font-family:"Exo 2",sans-serif;font-weight:500;font-size:26px;color:var(--blue);letter-spacing:.3px}
.easy-rule{left:37px;top:60px;width:500px;height:1px;background:#9bb3c2}
.step{position:absolute;top:74px;width:130px;text-align:center}
.step-icon{display:block;margin:0 auto}
.step-title{font-weight:600;font-size:12.5px;line-height:14px;margin-top:10px;color:var(--ink)}
.step-text{font-size:8.4px;line-height:10.5px;margin-top:6px;color:var(--muted)}
.perks{right:32px;top:224px;text-align:right;font-family:"Exo 2",sans-serif;font-style:italic;font-weight:700;color:var(--green);font-size:19px;line-height:24px}
.perks .first{border-bottom:1px solid #9bb3c2;padding-bottom:2px;margin-bottom:4px}
.seal{position:absolute;border-radius:50%;background:var(--white);border:7px solid var(--blue);display:flex;align-items:center;justify-content:center;text-align:center;box-shadow:0 3px 8px rgba(0,0,0,.25)}
.seal span{font-family:"Hind",sans-serif;font-weight:600;color:var(--blue);line-height:1.05}
.seal--process{left:218px;top:222px;width:144px;height:144px}
.seal--process span{font-size:19px}
.services{right:34px;top:350px;text-align:right;color:var(--white);font-weight:600}
.services li{list-style:none;position:relative;padding-right:20px;font-size:17.5px;line-height:24px}
.services li::after{content:"";position:absolute;right:0;top:7px;width:10px;height:10px;border-radius:50%;background:#e6eaee;box-shadow:inset 0 0 0 2px #5b6b78}
.services li.big{font-size:24px;line-height:26px}
.services li.sub{font-size:17.5px;line-height:20px;padding-bottom:4px}
.services li.sub::after{display:none}
.saying{left:28px;top:470px;font-family:"Exo 2",sans-serif;font-style:italic;font-weight:700;font-size:17px;color:var(--white)}
.saying-rule{left:220px;top:486px;width:298px;height:3px;background:var(--green)}
.quote{position:absolute;top:506px;width:150px;color:var(--white);font-size:8px;line-height:10.3px;text-align:justify}
.quote b{display:block;margin-top:8px;font-weight:700}
.quote + .quote{border-left:1px solid rgba(255,255,255,.35)}

/* solar page */
.seal--solar{left:34px;top:13px;width:148px;height:148px}
.seal--solar span{font-size:20px}
.headline{right:43px;top:20px;text-align:right}
.headline h1{font-family:"Roboto Condensed",sans-serif;font-weight:700;font-size:52px;line-height:56px;color:var(--green);letter-spacing:.5px}
.headline p{font-family:"Hind",sans-serif;font-weight:600;font-size:33px;line-height:36px;color:var(--ink);margin-top:-2px}
.promise{left:332px;top:200px;width:200px;color:var(--white)}
.promise h2{font-family:"Roboto Condensed",sans-serif;font-weight:700;font-size:30px;line-height:32px;letter-spacing:.4px}
.promise ul{margin-top:22px}
.promise li{list-style:none;position:relative;padding-left:24px;font-weight:600;font-size:21px;line-height:27px;margin-bottom:5px}
.promise li::before{content:"";position:absolute;left:2px;top:8px;width:12px;height:12px;border-radius:50%;background:#555}
.web{left:55px;top:392px;font-weight:600;font-size:17px;letter-spacing:.6px;color:var(--white)}
.install{left:27px;top:436px;color:var(--white);font-weight:600}
.install .l1{font-size:25px;line-height:32px}
.install .l2{font-size:19px;line-height:28px}
.install .l3{font-size:15.5px;line-height:24px}
.install .l3 strong{font-size:19px;font-weight:600}
.divider{left:227px;top:440px;width:1px;height:148px;background:rgba(255,255,255,.4)}
.why{left:253px;top:440px;width:266px;color:var(--white);font-size:8.6px;line-height:11.5px;text-align:justify}
.why p{margin-bottom:11px}
.why strong{font-weight:700}
.quote-cta{left:28px;top:630px}
.quote-cta h3{font-weight:600;font-size:20px;line-height:22px;color:var(--ink)}
.quote-cta .mail{font-weight:500;font-size:11.5px;color:var(--ink);margin-top:2px}
.quote-cta .addr{font-weight:500;font-size:10px;color:var(--ink);margin-top:8px}
.phone{right:32px;top:652px;display:flex;align-items:center;gap:10px}
.phone .dot{width:18px;height:18px;border-radius:50%;background:var(--white)}
.phone span{font-family:"Roboto Condensed",sans-serif;font-weight:700;font-size:30px;color:var(--white)}
</style>
</head>
<body>

<!-- Page one: process and testimonials -->
<section class="page page--process">
  <svg class="shapes" width="546" height="708" viewBox="0 0 546 708">
    <polygon points="0,226 420,330 400,338 0,254" fill="var(--green)"/>
    <polygon points="0,474 546,310 546,708 0,708" fill="var(--blue)"/>
    <line x1="230" y1="405" x2="546" y2="307" stroke="var(--grey)" stroke-width="5"/>
    <line x1="0" y1="474" x2="240" y2="402" stroke="var(--green)" stroke-width="2"/>
    <!-- step connectors -->
    <g fill="none" stroke="#9aa9b3" stroke-width="1" stroke-dasharray="2 2">
      <path d="M117,100 Q140,112 160,96"/><path d="M245,100 Q268,86 290,98"/><path d="M373,100 Q396,112 418,96"/>
    </g>
    <g fill="#9aa9b3"><path d="M160,96 l-5,0 l3,4z"/><path d="M290,98 l-4,-3 l0,5z"/><path d="M418,96 l-5,0 l3,4z"/></g>
  </svg>

  <h2 class="abs easy-title">WE MAKE IT EASY</h2>
  <div class="abs easy-rule"></div>

  <div class="step" style="left:10px">
    <svg class="step-icon" width="58" height="58" viewBox="0 0 58 58"><circle cx="29" cy="29" r="26" fill="#fff" stroke="var(--blue)" stroke-width="2.5"/><rect x="17" y="20" width="24" height="15" rx="1" fill="none" stroke="var(--blue)" stroke-width="1.8"/><line x1="14" y1="38" x2="44" y2="38" stroke="var(--blue)" stroke-width="2"/><circle cx="25" cy="26" r="3" fill="var(--blue)"/><circle cx="53" cy="29" r="4" fill="var(--green)"/></svg>
    <div class="step-title">Speak to a solar consultant</div>
    <div class="step-text">Meet with one of our energy consultants to review your solar options.</div>
  </div>
  <div class="step" style="left:138px">
    <svg class="step-icon" width="58" height="58" viewBox="0 0 58 58"><circle cx="29" cy="29" r="26" fill="#fff" stroke="var(--blue)" stroke-width="2.5"/><path d="M3,29 A26,26 0 0 1 29,3" fill="none" stroke="var(--green)" stroke-width="2.5"/><rect x="17" y="20" width="24" height="15" fill="none" stroke="var(--blue)" stroke-width="1.8"/><path d="M21,24h16M21,28h16M21,32h16M25,20v15M33,20v15" stroke="var(--blue)" stroke-width="1"/><line x1="29" y1="35" x2="29" y2="41" stroke="var(--blue)" stroke-width="2"/><circle cx="29" cy="55" r="4" fill="var(--green)"/></svg>
    <div class="step-title">We’ll design your solar panel system</div>
    <div class="step-text">We’ll finalize the details for tip top accuracy.</div>
  </div>
  <div class="step" style="left:264px">
    <svg class="step-icon" width="58" height="58" viewBox="0 0 58 58"><circle cx="29" cy="29" r="26" fill="#fff" stroke="var(--green)" stroke-width="2.5"/><rect x="19" y="17" width="15" height="20" fill="none" stroke="var(--blue)" stroke-width="1.8"/><circle cx="36" cy="35" r="7" fill="#fff" stroke="var(--blue)" stroke-width="1.8"/><path d="M36,31v4h3" stroke="var(--blue)" stroke-width="1.5" fill="none"/><circle cx="3" cy="29" r="4" fill="var(--green)"/></svg>
    <div class="step-title">Schedule your 1 day install</div>
    <div class="step-text">Let us do the heavy lifting as you watch your home upgrade to solar.</div>
  </div>
  <div class="step" style="left:396px">
    <svg class="step-icon" width="58" height="58" viewBox="0 0 58 58"><circle cx="29" cy="29" r="26" fill="#fff" stroke="var(--green)" stroke-width="2.5"/><circle cx="29" cy="27" r="8" fill="none" stroke="var(--green)" stroke-width="2"/><path d="M26,35h6v4h-6z" fill="var(--green)"/><path d="M29,12v4M16,27h-4M46,27h-4M19,17l3,3M39,17l-3,3" stroke="var(--green)" stroke-width="1.5"/><circle cx="29" cy="3" r="4" fill="var(--green)"/></svg>
    <div class="step-title">Start saving on your electricity bill</div>
    <div class="step-text">Watch your electric bill lower and your energy savings build for year to come.</div>
  </div>

  <div class="photo" role="img" aria-label="Family silhouetted at sunset, a child on a parent's shoulders" style="left:0;top:0;width:546px;height:708px;clip-path:polygon(0 254px,400px 338px,400px 354px,0 474px);background:linear-gradient(100deg,#3c3a4a 0%,#b9703e 45%,#f5c77a 80%,#fbe6b5 100%)"></div>

  <div class="abs perks"><div class="first">Zero upfront Cost</div><div>Lower monthly</div><div>Energy Costs</div></div>
  <div class="seal seal--process"><span>Kestrel<br>Roofpower</span></div>

  <ul class="abs services">
    <li class="big">Reduce</li>
    <li class="sub">Energy Costs</li>
    <li>Savings Beyond Solar</li>
    <li>What will my Electricity Cost?</li>
    <li>Energy Monitoring</li>
  </ul>

  <div class="abs saying">What People are saying...</div>
  <div class="abs saying-rule"></div>

  <div class="quote" style="left:27px;padding-right:8px">My husband and I decided to go solar after 3 of our neighbors did. After having it I don't know why we waited so long!<b>Marisa K.</b></div>
  <div class="quote" style="left:177px;padding:0 8px;width:178px">I had met with a few different companies and didn't care for their options. Our team had an option we liked and we went for it! Its been working great for us.<b>Owen and Petra L.</b></div>
  <div class="quote" style="left:355px;padding-left:8px;width:168px">We were a bit nervous to go solar.. after our consultation with Theo it was very easy to see that solar was our best option. Now we are saving tons on our electric bill! Thanks !<b>Ray and Nell V.</b></div>

  <div class="photo" role="img" aria-label="Brick family home with rooftop solar panels and wind turbines" style="left:0;top:572px;width:194px;height:136px;background:linear-gradient(180deg,#b9cbe0 0%,#a25a3c 55%,#5d8d3a 100%)"></div>
  <div class="photo" role="img" aria-label="Aerial view of a large roof covered with solar panels" style="left:198px;top:572px;width:156px;height:136px;background:linear-gradient(160deg,#6f8f5a 0%,#2c4f8a 45%,#d9d4c6 100%)"></div>
  <div class="photo" role="img" aria-label="Tiled roof with solar panels and wind turbines against a bright sky" style="left:358px;top:572px;width:188px;height:136px;background:linear-gradient(180deg,#dfe9f2 0%,#9ab6cf 40%,#3e4f6a 65%,#a24a2a 100%)"></div>
</section>

<!-- Page two: solar offer and our why -->
<section class="page page--solar">
  <div class="photo" role="img" aria-label="White two-storey house with a dark solar-panel roof at dusk" style="left:0;top:106px;width:546px;height:300px;background:linear-gradient(180deg,#c9d6de 0%,#3a3d44 35%,#e8e6e0 60%,#6f8d48 100%)"></div>
  <svg class="shapes" width="546" height="708" viewBox="0 0 546 708">
    <rect x="0" y="398" width="546" height="310" fill="var(--blue)"/>
    <polygon points="318,159 527,191 527,419 318,419" fill="var(--green)"/>
    <path d="M38,398 H262 L248,416 Q242,424 230,424 H60 Q48,424 44,414 Z" fill="var(--green)"/>
  </svg>

  <div class="seal seal--solar"><span>Kestrel<br>Roofpower</span></div>
  <div class="abs headline"><h1>SOLAR ENERGY</h1><p>$0 Upfront Cost</p></div>

  <div class="abs promise">
    <h2>BRINGING THE POWER OF THE SUN FOR YOU</h2>
    <ul><li>Zero upfront Cost.</li><li>Lower monthly Energy Costs</li></ul>
  </div>

  <div class="abs web">KestrelRoofpower.example</div>

  <div class="abs install">
    <div class="l1">We install</div>
    <div class="l2">Residential Solar</div>
    <div class="l3">and this will be used for</div>
    <div class="l2">Military base housing</div>
    <div class="l3">and other <strong>govt. projects</strong></div>
    <div class="l3" style="font-size:17px">on the Residential Home</div>
    <div class="l3" style="font-size:17px">Communities.</div>
  </div>
  <div class="abs divider"></div>

  <div class="abs why">
    <p>We are on a mission to empower home owners and businesses to power their lives with better, less expensive, cleaner energy creating a world that is powered by the sun.</p>
    <p>With solar, homeowners are saving money while dramatically lessening the amount of pollution released into the atmosphere. We believe that, together, we can create a planet run by the sun.</p>
    <p>Everyone should have the freedom to choose where they get their energy and be able to control their energy costs. Homeowners across the nation rely on us to <strong>provide $0 upfront cost</strong> options in upgrading their home to <strong>solar energy in a way that saves them money on monthly electrical costs.</strong></p>
    <p>Smart and forward thinking, Solar allows you the ability to lower your energy bills and avoid the costly rate increases.</p>
  </div>

  <div class="abs quote-cta">
    <h3>Get a free quote</h3>
    <div class="mail">email: hello@kestrelroofpower.example</div>
    <div class="addr">18 Harrow Ln., Suite 4-B, Fenwick NJ 08999</div>
  </div>
  <div class="abs phone"><div class="dot"></div><span>(800) 555-0147</span></div>
</section>

</body>
</html>
```